Powerpoint Presentation Template

Kindly design a business class Powepoint Presentation template for our business use. Please stick to our company colours or even pictures as shown on our website and Logo

```html
<!DOCTYPE html>
<html lang="en">
<head>
<meta charset="utf-8">
<title>Kestrel Properties – Presentation Template</title>
<link href="https://fonts.googleapis.com/css2?family=Roboto:wght@300;400;700&display=swap" rel="stylesheet">
<style>
:root{
  --red:#8c2b1f;
  --red-dark:#6e1f16;
  --ink:#2f2f2f;
  --grey:#8a8a8a;
  --line:#d8d8d8;
  --paper:#ffffff;
  --canvas:#ebebeb;
  --sky:linear-gradient(180deg,#3d6db3 0%,#8fb2dc 38%,#e4e4e0 52%,#a9a9a4 78%,#6f6f6a 100%);
  --site:linear-gradient(160deg,#b88b62 0%,#8e6a4b 50%,#5d5548 100%);
  --interior:linear-gradient(150deg,#c9c3b8 0%,#9a9287 60%,#5e5a55 100%);
  --portrait:linear-gradient(180deg,#d9d9d9 0%,#a6a6a6 100%);
}
*{box-sizing:border-box;margin:0;padding:0}
html,body{width:790px;height:1200px;overflow:hidden;background:var(--canvas);font-family:'Roboto',Arial,sans-serif;color:var(--ink)}
.sheet{display:grid;grid-template-columns:repeat(3,250px);grid-auto-rows:140px;gap:7.5px 7px;padding:12px 14px}
.slide{position:relative;background:var(--paper);overflow:hidden;box-shadow:0 1px 2px rgba(0,0,0,.12)}
.slide-title{position:absolute;left:12px;top:14px;font-size:6.4px;letter-spacing:.1px;color:#444;font-weight:400}
.slide-title b{color:var(--red);font-weight:700;border-bottom:.7px solid var(--red)}
.brand{position:absolute;right:8px;top:6px;font-size:4.2px;font-weight:700;color:var(--red);text-align:right;line-height:1.05;letter-spacing:.2px}
.footer{position:absolute;left:0;right:0;bottom:0;height:4px;background:var(--red);font-size:2.2px;color:#fff;padding-left:10px;line-height:4px}
.footer::after{content:"";position:absolute;right:0;top:0;width:18px;height:4px;background:var(--ink)}
.photo{position:absolute;background:var(--sky)}
.photo.site{background:var(--site)}
.photo.interior{background:var(--interior)}
.photo.portrait{background:var(--portrait)}
.heading{font-size:3.2px;font-weight:700;color:var(--red);margin-bottom:1.5px}
.body-text{font-size:2.5px;line-height:1.55;color:var(--grey)}
.icon-box{width:10px;height:10px;background:var(--red);display:flex;align-items:center;justify-content:center;flex:none}
.icon-box svg{width:6px;height:6px}
.icon-item{position:absolute;display:flex;gap:4px;width:70px}
.faint{position:absolute;inset:0;background:linear-gradient(180deg,#f6f6f6,#e9e9e9);opacity:.9}
.brand-box{position:absolute;border:.8px solid var(--red);color:var(--red);font-weight:700;text-align:center;display:flex;flex-direction:column;justify-content:center;line-height:1.15}
.name-tag{position:absolute;left:0;right:0;bottom:0;background:var(--red);color:#fff;font-size:2.4px;text-align:center;padding:.8px 0}
table.grid{position:absolute;left:24px;top:32px;width:202px;border-collapse:collapse;font-size:2.2px;color:var(--grey)}
table.grid td,table.grid th{height:9px;text-align:center;border-bottom:.4px solid var(--line)}
table.grid th{background:var(--red);color:#fff;font-weight:400}
table.grid td.row-head{background:#333;color:#ddd;text-align:left;padding-left:4px;width:46px}
table.grid tr:nth-child(even) td:not(.row-head){background:#f3f3f3}
.dot{display:inline-block;width:3.6px;height:3.6px;border-radius:50%;background:var(--red)}
</style>
</head>
<body>
<svg width="0" height="0" style="position:absolute">
  <symbol id="i-home" viewBox="0 0 12 12"><path d="M2 6 6 2.5 10 6V10H2Z" fill="none" stroke="#fff" stroke-width="1.1"/></symbol>
  <symbol id="i-doc" viewBox="0 0 12 12"><rect x="2.5" y="2" width="7" height="8" fill="none" stroke="#fff" stroke-width="1.1"/><path d="M4 4.5h4M4 6.5h4M4 8.3h2.5" stroke="#fff" stroke-width=".8"/></symbol>
  <symbol id="i-chart" viewBox="0 0 12 12"><path d="M2 10h8M3.5 9V6M6 9V3.5M8.5 9V5" stroke="#fff" stroke-width="1.1"/></symbol>
  <symbol id="i-search" viewBox="0 0 12 12"><circle cx="5.3" cy="5.3" r="2.8" fill="none" stroke="#fff" stroke-width="1.1"/><path d="M7.4 7.4 10 10" stroke="#fff" stroke-width="1.2"/></symbol>
  <symbol id="i-badge" viewBox="0 0 12 12"><circle cx="6" cy="5" r="3" fill="none" stroke="#fff" stroke-width="1.1"/><path d="M4.3 7.5 3.5 10.5 6 9.3 8.5 10.5 7.7 7.5" fill="none" stroke="#fff" stroke-width=".9"/></symbol>
</svg>

<main class="sheet">

<!-- 1 cover -->
<section class="slide">
  <div class="faint" role="img" aria-label="Faded photo of a modern residential building"></div>
  <div class="brand-box" style="left:86px;top:52px;width:78px;height:36px;font-size:6.5px;background:#fff">Kestrel<br>Properties</div>
</section>

<!-- 2 title -->
<section class="slide">
  <div class="brand-box" style="left:18px;top:18px;width:48px;height:24px;font-size:4.6px">Kestrel<br>Properties</div>
  <div style="position:absolute;left:18px;top:90px;font-size:6.6px;font-weight:700;color:var(--red)">PRESENTATION <span style="font-weight:400;color:#444">TITLE</span></div>
  <div class="body-text" style="position:absolute;left:18px;top:122px;font-size:2.3px">Presented by <b style="color:var(--red)">John Doe</b><br>July 15, 2024 · Marlow Ridge</div>
  <div class="photo" style="left:100px;top:0;width:150px;height:140px;clip-path:polygon(28% 0,100% 0,100% 100%,0 100%)" role="img" aria-label="Photo of a three-storey apartment block with scaffolding"></div>
  <svg style="position:absolute;left:0;top:0" width="250" height="140"><polygon points="0,100 0,140 40,140" fill="var(--red)"/><polygon points="232,0 250,0 250,40" fill="var(--red)"/></svg>
</section>

<!-- 3 contents -->
<section class="slide">
  <div class="brand">Kestrel<br>Properties</div>
  <div style="position:absolute;left:16px;top:62px;font-size:6.4px;color:#444"><b style="color:var(--red)">TABLE</b> OF CONTENT</div>
  <div class="body-text" style="position:absolute;left:16px;top:74px;width:70px">Short notes that guide the reader through each part of this deck.</div>
  <div style="position:absolute;left:106px;top:36px;width:62px">
    <div class="heading">01. Heading text</div><div class="body-text" style="margin-bottom:5px">Brief line of text here.</div>
    <div class="heading">02. Heading text</div><div class="body-text" style="margin-bottom:5px">Brief line of text here.</div>
    <div class="heading">03. Heading text</div><div class="body-text" style="margin-bottom:5px">Brief line of text here.</div>
    <div class="heading">04. Heading text</div><div class="body-text">Brief line of text here.</div>
  </div>
  <div style="position:absolute;left:172px;top:36px;width:62px">
    <div class="heading">05. Heading text</div><div class="body-text" style="margin-bottom:5px">Brief line of text here.</div>
    <div class="heading">06. Heading text</div><div class="body-text" style="margin-bottom:5px">Brief line of text here.</div>
    <div class="heading">07. Heading text</div><div class="body-text" style="margin-bottom:5px">Brief line of text here.</div>
    <div class="heading">08. Heading text</div><div class="body-text">Brief line of text here.</div>
  </div>
</section>

<!-- 4 our company -->
<section class="slide">
  <div class="photo" style="left:0;top:0;width:250px;height:86px" role="img" aria-label="Photo of white modern townhouses under a blue sky"></div>
  <div class="brand">Kestrel<br>Properties</div>
  <div style="position:absolute;left:0;top:32px;width:112px;height:54px;background:rgba(140,43,31,.93);padding:11px 0 0 19px;color:#fff">
    <div style="font-size:6.2px"><b>OUR</b> COMPANY</div>
    <div style="font-size:2.6px;line-height:1.5;margin-top:3px;font-style:italic;width:78px">"We build homes and offices that last, with care in every detail."</div>
  </div>
  <div class="icon-item" style="left:20px;top:95px"><div class="icon-box"><svg><use href="#i-chart"/></svg></div><div><div class="heading">Heading text</div><div class="body-text">Short text about this point.</div></div></div>
  <div class="icon-item" style="left:96px;top:95px"><div class="icon-box"><svg><use href="#i-home"/></svg></div><div><div class="heading">Heading text</div><div class="body-text">Short text about this point.</div></div></div>
  <div class="icon-item" style="left:172px;top:95px"><div class="icon-box"><svg><use href="#i-badge"/></svg></div><div><div class="heading">Heading text</div><div class="body-text">Short text about this point.</div></div></div>
  <div class="footer">www.kestrelprops.co.za</div>
</section>

<!-- 5 full photo -->
<section class="slide">
  <div class="photo" style="inset:0" role="img" aria-label="Photo of a curved-roof apartment building on a clear day"></div>
  <div class="brand">Kestrel<br>Properties</div>
  <div style="position:absolute;left:0;right:0;bottom:4px;height:14px;background:rgba(110,31,22,.8);color:#fff;font-size:2.4px;line-height:1.5;padding:2.5px 19px">A short caption about this photo and the project shown above it.</div>
  <div class="footer">www.kestrelprops.co.za</div>
</section>

<!-- 6 one column -->
<section class="slide">
  <div class="brand">Kestrel<br>Properties</div>
  <div class="slide-title" style="left:19px"><b>ONE COLLUMN</b> TEXT SLIDE</div>
  <div class="body-text" style="position:absolute;left:19px;top:32px;width:212px">
    <p style="margin-bottom:3px">Kestrel Properties designs and builds homes, offices and retail space across the region. We plan each project with care and manage every stage from site work to handover, so clients get quality work on time and within budget. Our team brings years of hands-on skill to each build.</p>
    <p style="margin-bottom:3px">We work closely with owners, architects and local suppliers to deliver spaces that are safe, efficient and built to last. Every site follows clear safety rules and regular quality checks.</p>
    <p>From first sketch to final key, we keep you informed and involved. This is why our clients return to us for new projects year after year.</p>
  </div>
  <div class="footer">www.kestrelprops.co.za</div>
</section>

<!-- 7 two column -->
<section class="slide">
  <div class="brand">Kestrel<br>Properties</div>
  <div class="slide-title" style="left:19px"><b>TWO COLLUMN</b> TEXT SLIDE</div>
  <div class="body-text" style="position:absolute;left:19px;top:32px;width:100px">
    <p style="margin-bottom:4px">We design and build homes, offices and retail space. Each project is planned with care and managed from site work to handover.</p>
    <p>Our team brings years of hands-on skill to every build we take on.</p>
  </div>
  <div class="body-text" style="position:absolute;left:131px;top:32px;width:100px">
    <p style="margin-bottom:4px">We work with owners, architects and local suppliers to deliver spaces that are safe, efficient and built to last.</p>
    <p>Clear safety rules and regular quality checks guide every site.</p>
  </div>
  <div class="footer">www.kestrelprops.co.za</div>
</section>

<!-- 8 bullets -->
<section class="slide">
  <div class="brand">Kestrel<br>Properties</div>
  <div class="slide-title" style="left:19px"><b>BULLET</b> TEXT SLIDE</div>
  <div style="position:absolute;left:19px;top:32px;width:100px">
    <div class="heading">• Heading text</div><div class="body-text" style="margin-bottom:4px">Short line of text that explains this bullet point.</div>
    <div class="heading">• Heading text</div><div class="body-text" style="margin-bottom:4px">Short line of text that explains this bullet point.</div>
    <div class="heading">• Heading text</div><div class="body-text">Short line of text that explains this bullet point.</div>
  </div>
  <div style="position:absolute;left:131px;top:32px;width:100px">
    <div class="heading">• Heading text</div><div class="body-text" style="margin-bottom:4px">Short line of text that explains this bullet point.</div>
    <div class="heading">• Heading text</div><div class="body-text" style="margin-bottom:4px">Short line of text that explains this bullet point.</div>
    <div class="heading">• Heading text</div><div class="body-text">Short line of text that explains this bullet point.</div>
  </div>
  <div class="footer">www.kestrelprops.co.za</div>
</section>

<!-- 9 what we do -->
<section class="slide">
  <div class="brand">Kestrel<br>Properties</div>
  <div class="slide-title" style="left:19px"><b>WHAT</b> WE DO</div>
  <div class="photo" style="left:0;top:31px;width:250px;height:50px" role="img" aria-label="Photo of a row of modern houses"></div>
  <div style="position:absolute;left:10px;right:10px;top:76px;display:flex;justify-content:space-around;text-align:center">
    <div style="width:48px"><div class="icon-box" style="margin:0 auto 4px"><svg><use href="#i-chart"/></svg></div><div class="heading">Heading text</div><div class="body-text">Short text for this point here.</div></div>
    <div style="width:48px"><div class="icon-box" style="margin:0 auto 4px"><svg><use href="#i-doc"/></svg></div><div class="heading">Heading text</div><div class="body-text">Short text for this point here.</div></div>
    <div style="width:48px"><div class="icon-box" style="margin:0 auto 4px"><svg><use href="#i-home"/></svg></div><div class="heading">Heading text</div><div class="body-text">Short text for this point here.</div></div>
    <div style="width:48px"><div class="icon-box" style="margin:0 auto 4px"><svg><use href="#i-search"/></svg></div><div class="heading">Heading text</div><div class="body-text">Short text for this point here.</div></div>
  </div>
  <div class="footer">www.kestrelprops.co.za</div>
</section>

<!-- 10 our service -->
<section class="slide">
  <div class="faint" role="img" aria-label="Faded photo of a building"></div>
  <div class="brand">Kestrel<br>Properties</div>
  <div class="slide-title" style="left:19px"><b>OUR</b> SERVICE</div>
  <div class="icon-item" style="left:19px;top:44px"><div class="icon-box"><svg><use href="#i-chart"/></svg></div><div><div class="heading">Heading text</div><div class="body-text">Short text about this service.</div></div></div>
  <div class="icon-item" style="left:96px;top:44px"><div class="icon-box"><svg><use href="#i-home"/></svg></div><div><div class="heading">Heading text</div><div class="body-text">Short text about this service.</div></div></div>
  <div class="icon-item" style="left:173px;top:44px"><div class="icon-box"><svg><use href="#i-badge"/></svg></div><div><div class="heading">Heading text</div><div class="body-text">Short text about this service.</div></div></div>
  <div class="icon-item" style="left:19px;top:81px"><div class="icon-box"><svg><use href="#i-doc"/></svg></div><div><div class="heading">Heading text</div><div class="body-text">Short text about this service.</div></div></div>
  <div class="icon-item" style="left:96px;top:81px"><div class="icon-box"><svg><use href="#i-home"/></svg></div><div><div class="heading">Heading text</div><div class="body-text">Short text about this service.</div></div></div>
  <div class="icon-item" style="left:173px;top:81px"><div class="icon-box"><svg><use href="#i-search"/></svg></div><div><div class="heading">Heading text</div><div class="body-text">Short text about this service.</div></div></div>
  <div class="footer">www.kestrelprops.co.za</div>
</section>

<!-- 11 history -->
<section class="slide">
  <div class="brand">Kestrel<br>Properties</div>
  <div class="slide-title" style="left:19px"><b>OUR</b> HISTORY</div>
  <svg style="position:absolute;left:0;top:66px" width="250" height="8">
    <line x1="0" y1="4" x2="250" y2="4" stroke="var(--red)" stroke-width=".6" stroke-dasharray="1.5 1"/>
    <g fill="#fff" stroke="var(--grey)" stroke-width=".5">
      <circle cx="28" cy="4" r="1.6"/><circle cx="50" cy="4" r="1.6"/><circle cx="71" cy="4" r="1.6"/><circle cx="93" cy="4" r="1.6"/><circle cx="114" cy="4" r="1.6"/><circle cx="136" cy="4" r="1.6"/><circle cx="157" cy="4" r="1.6"/><circle cx="179" cy="4" r="1.6"/><circle cx="200" cy="4" r="1.6"/><circle cx="222" cy="4" r="1.6"/>
    </g>
  </svg>
  <div style="position:absolute;left:30px;top:44px;display:flex;gap:3px;text-align:center">
    <div style="width:40px"><div class="heading">Heading text</div><div class="body-text">A short note on this year.</div></div>
    <div style="width:40px"><div class="heading">Heading text</div><div class="body-text">A short note on this year.</div></div>
    <div style="width:40px"><div class="heading">Heading text</div><div class="body-text">A short note on this year.</div></div>
    <div style="width:40px"><div class="heading">Heading text</div><div class="body-text">A short note on this year.</div></div>
    <div style="width:40px"><div class="heading">Heading text</div><div class="body-text">A short note on this year.</div></div>
  </div>
  <div style="position:absolute;left:8px;top:81px;display:flex;gap:3px;text-align:center">
    <div style="width:40px"><div class="heading">Heading text</div><div class="body-text">A short note on this year.</div></div>
    <div style="width:40px"><div class="heading">Heading text</div><div class="body-text">A short note on this year.</div></div>
    <div style="width:40px"><div class="heading">Heading text</div><div class="body-text">A short note on this year.</div></div>
    <div style="width:40px"><div class="heading">Heading text</div><div class="body-text">A short note on this year.</div></div>
    <div style="width:40px"><div class="heading">Heading text</div><div class="body-text">A short note on this year.</div></div>
  </div>
  <div class="footer">www.kestrelprops.co.za</div>
</section>

<!-- 12 team grid -->
<section class="slide">
  <div class="brand">Kestrel<br>Properties</div>
  <div class="slide-title" style="left:19px"><b>OUR</b> TEAM</div>
  <div style="position:absolute;left:30px;top:32px;display:grid;grid-template-columns:repeat(4,28px);column-gap:24px;row-gap:16px">
    <div class="photo portrait" style="position:relative;height:38px" role="img" aria-label="Team member portrait"><div class="name-tag">Name Here</div></div>
    <div class="photo portrait" style="position:relative;height:38px" role="img" aria-label="Team member portrait"><div class="name-tag">Name Here</div></div>
    <div class="photo portrait" style="position:relative;height:38px" role="img" aria-label="Team member portrait"><div class="name-tag">Name Here</div></div>
    <div class="photo portrait" style="position:relative;height:38px" role="img" aria-label="Team member portrait"><div class="name-tag">Name Here</div></div>
    <div class="photo portrait" style="position:relative;height:38px" role="img" aria-label="Team member portrait"><div class="name-tag">Name Here</div></div>
    <div class="photo portrait" style="position:relative;height:38px" role="img" aria-label="Team member portrait"><div class="name-tag">Name Here</div></div>
    <div class="photo portrait" style="position:relative;height:38px" role="img" aria-label="Team member portrait"><div class="name-tag">Name Here</div></div>
    <div class="photo portrait" style="position:relative;height:38px" role="img" aria-label="Team member portrait"><div class="name-tag">Name Here</div></div>
  </div>
  <div class="footer">www.kestrelprops.co.za</div>
</section>

<!-- 13 team detail -->
<section class="slide">
  <div class="brand">Kestrel<br>Properties</div>
  <div class="slide-title" style="left:19px"><b>OUR</b> TEAM</div>
  <div style="position:absolute;left:13px;top:40px;display:flex;gap:10px">
    <div style="width:70px">
      <div style="display:flex;gap:3px"><div class="photo portrait" style="position:relative;width:30px;height:28px" role="img" aria-label="Team member portrait"></div><div><div class="heading">Name Here</div><div class="body-text">Job title<br>Short note here.</div><div style="margin-top:2px;display:flex;gap:1px"><span class="dot"></span><span class="dot"></span><span class="dot"></span></div></div></div>
      <div class="body-text" style="margin-top:5px">A few lines about this person and the role they play on our team.</div>
    </div>
    <div style="width:70px">
      <div style="display:flex;gap:3px"><div class="photo portrait" style="position:relative;width:30px;height:28px" role="img" aria-label="Team member portrait"></div><div><div class="heading">Name Here</div><div class="body-text">Job title<br>Short note here.</div><div style="margin-top:2px;display:flex;gap:1px"><span class="dot"></span><span class="dot"></span><span class="dot"></span></div></div></div>
      <div class="body-text" style="margin-top:5px">A few lines about this person and the role they play on our team.</div>
    </div>
    <div style="width:70px">
      <div style="display:flex;gap:3px"><div class="photo portrait" style="position:relative;width:30px;height:28px" role="img" aria-label="Team member portrait"></div><div><div class="heading">Name Here</div><div class="body-text">Job title<br>Short note here.</div><div style="margin-top:2px;display:flex;gap:1px"><span class="dot"></span><span class="dot"></span><span class="dot"></span></div></div></div>
      <div class="body-text" style="margin-top:5px">A few lines about this person and the role they play on our team.</div>
    </div>
  </div>
  <div class="footer">www.kestrelprops.co.za</div>
</section>

<!-- 14 product two -->
<section class="slide">
  <div class="brand">Kestrel<br>Properties</div>
  <div class="slide-title" style="left:19px"><b>OUR</b> PRODUCT</div>
  <div class="photo" style="left:19px;top:34px;width:102px;height:52px" role="img" aria-label="Photo of a modern office building"><div class="name-tag">Heading text</div></div>
  <div class="photo site" style="left:129px;top:34px;width:102px;height:52px" role="img" aria-label="Photo of road works on a building site"><div class="name-tag">Heading text</div></div>
  <div class="body-text" style="position:absolute;left:19px;top:90px;width:102px">Short text about this product and what it offers our clients.</div>
  <div class="body-text" style="position:absolute;left:129px;top:90px;width:102px">Short text about this product and what it offers our clients.</div>
  <div class="footer">www.kestrelprops.co.za</div>
</section>

<!-- 15 product three -->
<section class="slide">
  <div class="brand">Kestrel<br>Properties</div>
  <div class="slide-title" style="left:19px"><b>OUR</b> PRODUCT</div>
  <div class="photo site" style="left:19px;top:38px;width:68px;height:46px" role="img" aria-label="Photo of foundation trenches"></div>
  <div class="photo site" style="left:91px;top:38px;width:68px;height:46px" role="img" aria-label="Photo of excavated ground with steel"></div>
  <div class="photo site" style="left:163px;top:38px;width:68px;height:46px" role="img" aria-label="Photo of a concrete slab being prepared"></div>
  <div style="position:absolute;left:19px;top:88px;width:68px"><div class="heading">Heading text</div><div class="body-text">Short text about this stage of the build.</div></div>
  <div style="position:absolute;left:91px;top:88px;width:68px"><div class="heading">Heading text</div><div class="body-text">Short text about this stage of the build.</div></div>
  <div style="position:absolute;left:163px;top:88px;width:68px"><div class="heading">Heading text</div><div class="body-text">Short text about this stage of the build.</div></div>
  <div class="footer">www.kestrelprops.co.za</div>
</section>

<!-- 16 product mixed -->
<section class="slide">
  <div class="brand">Kestrel<br>Properties</div>
  <div class="slide-title" style="left:19px"><b>OUR</b> PRODUCT</div>
  <div class="photo" style="left:19px;top:34px;width:96px;height:56px" role="img" aria-label="Photo of a double-storey house with a garden"></div>
  <div class="photo site" style="left:117px;top:34px;width:44px;height:18px" role="img" aria-label="Photo of a truck on site"></div>
  <div class="photo interior" style="left:117px;top:54px;width:44px;height:17px" role="img" aria-label="Photo of an office interior"></div>
  <div class="photo interior" style="left:117px;top:73px;width:44px;height:17px" role="img" aria-label="Photo of a lounge interior"></div>
  <div style="position:absolute;left:166px;top:34px;width:66px">
    <div class="heading">• Heading text</div><div class="body-text" style="margin-bottom:3px">Short text about this item.</div>
    <div class="heading">• Heading text</div><div class="body-text" style="margin-bottom:3px">Short text about this item.</div>
    <div class="heading">• Heading text</div><div class="body-text">Short text about this item.</div>
  </div>
  <div style="position:absolute;left:19px;top:94px;width:212px"><div class="heading">• Heading text</div><div class="body-text">Longer text about the products we build, the quality we aim for and the value each project brings to the people who live and work in it.</div></div>
  <div class="footer">www.kestrelprops.co.za</div>
</section>

<!-- 17 portfolio collage -->
<section class="slide">
  <div class="brand">Kestrel<br>Properties</div>
  <div class="slide-title" style="left:19px"><b>OUR</b> PORTFOLIO</div>
  <div class="photo" style="left:7px;top:31px;width:86px;height:64px" role="img" aria-label="Photo of modern townhouses"></div>
  <div class="photo site" style="left:95px;top:31px;width:47px;height:30px" role="img" aria-label="Photo of a building site"></div>
  <div class="photo site" style="left:144px;top:31px;width:99px;height:68px" role="img" aria-label="Photo of site works"></div>
  <div class="photo interior" style="left:95px;top:63px;width:47px;height:36px" role="img" aria-label="Photo of an interior"></div>
  <div class="photo site" style="left:7px;top:97px;width:86px;height:34px" role="img" aria-label="Photo of houses under construction"></div>
  <div class="photo site" style="left:95px;top:101px;width:47px;height:30px" role="img" aria-label="Photo of pipes and trenches"></div>
  <div class="photo site" style="left:144px;top:101px;width:99px;height:30px" role="img" aria-label="Photo of a concrete slab"></div>
  <div class="footer">www.kestrelprops.co.za</div>
</section>

<!-- 18 portfolio grid -->
<section class="slide">
  <div class="brand">Kestrel<br>Properties</div>
  <div class="slide-title" style="left:19px"><b>OUR</b> PORTFOLIO</div>
  <div style="position:absolute;left:7px;top:31px;display:grid;grid-template-columns:repeat(4,57px);grid-auto-rows:32px;gap:2px">
    <div class="photo interior" style="position:relative" role="img" aria-label="Project photo"></div>
    <div class="photo" style="position:relative" role="img" aria-label="Project photo"></div>
    <div class="photo interior" style="position:relative" role="img" aria-label="Project photo"></div>
    <div class="photo site" style="position:relative" role="img" aria-label="Project photo"></div>
    <div class="photo site" style="position:relative" role="img" aria-label="Project photo"></div>
    <div class="photo" style="position:relative" role="img" aria-label="Project photo"></div>
    <div class="photo" style="position:relative" role="img" aria-label="Project photo"></div>
    <div class="photo interior" style="position:relative" role="img" aria-label="Project photo"></div>
    <div class="photo site" style="position:relative" role="img" aria-label="Project photo"></div>
    <div class="photo site" style="position:relative" role="img" aria-label="Project photo"></div>
    <div class="photo site" style="position:relative" role="img" aria-label="Project photo"></div>
    <div class="photo" style="position:relative" role="img" aria-label="Project photo"></div>
  </div>
  <div class="footer">www.kestrelprops.co.za</div>
</section>

<!-- 19 donuts -->
<section class="slide">
  <div class="brand">Kestrel<br>Properties</div>
  <div class="slide-title" style="left:19px"><b>CHART</b> AND DIAGRAM SLIDE</div>
  <div style="position:absolute;left:19px;top:42px;display:flex;gap:13px;text-align:center">
    <div style="width:62px"><svg width="34" height="34" viewBox="0 0 34 34"><circle cx="17" cy="17" r="14" fill="none" stroke="#333" stroke-width="2.4"/><circle cx="17" cy="17" r="14" fill="none" stroke="var(--red)" stroke-width="2.4" stroke-dasharray="52.8 35.2" transform="rotate(-90 17 17)"/><text x="17" y="19" font-size="5" text-anchor="middle" fill="var(--red)" font-family="Roboto,sans-serif">60%</text></svg><div class="heading" style="margin-top:4px">Heading text</div><div class="body-text">Short text about this figure and its meaning.</div></div>
    <div style="width:62px"><svg width="34" height="34" viewBox="0 0 34 34"><circle cx="17" cy="17" r="14" fill="none" stroke="#333" stroke-width="2.4"/><circle cx="17" cy="17" r="14" fill="none" stroke="var(--red)" stroke-width="2.4" stroke-dasharray="52.8 35.2" transform="rotate(-90 17 17)"/><text x="17" y="19" font-size="5" text-anchor="middle" fill="var(--red)" font-family="Roboto,sans-serif">60%</text></svg><div class="heading" style="margin-top:4px">Heading text</div><div class="body-text">Short text about this figure and its meaning.</div></div>
    <div style="width:62px"><svg width="34" height="34" viewBox="0 0 34 34"><circle cx="17" cy="17" r="14" fill="none" stroke="#333" stroke-width="2.4"/><circle cx="17" cy="17" r="14" fill="none" stroke="var(--red)" stroke-width="2.4" stroke-dasharray="52.8 35.2" transform="rotate(-90 17 17)"/><text x="17" y="19" font-size="5" text-anchor="middle" fill="var(--red)" font-family="Roboto,sans-serif">60%</text></svg><div class="heading" style="margin-top:4px">Heading text</div><div class="body-text">Short text about this figure and its meaning.</div></div>
  </div>
  <div class="footer">www.kestrelprops.co.za</div>
</section>

<!-- 20 table -->
<section class="slide">
  <div class="brand">Kestrel<br>Properties</div>
  <div class="slide-title" style="left:19px"><b>CHART</b> AND DIAGRAM SLIDE</div>
  <table class="grid">
    <tr><th style="background:#333">Item</th><th>Plan A</th><th>Plan B</th><th>Plan C</th><th>Plan D</th></tr>
    <tr><td class="row-head">Design</td><td><span class="dot"></span></td><td><span class="dot"></span></td><td><span class="dot"></span></td><td><span class="dot"></span></td></tr>
    <tr><td class="row-head">Build</td><td><span class="dot"></span></td><td><span class="dot"></span></td><td><span class="dot"></span></td><td><span class="dot"></span></td></tr>
    <tr><td class="row-head">Permits</td><td>Yes</td><td>Yes</td><td>Yes</td><td>Yes</td></tr>
    <tr><td class="row-head">Finish</td><td>Yes</td><td>Yes</td><td>Yes</td><td>Yes</td></tr>
    <tr><td class="row-head">Time</td><td>1.2</td><td>2.2</td><td>3.4</td><td>4.6</td></tr>
    <tr><td class="row-head">Cost</td><td>1.2</td><td>2.2</td><td>3.4</td><td>4.6</td></tr>
  </table>
  <div class="body-text" style="position:absolute;left:24px;top:100px;width:202px">Short note that explains the table above and how to read it.</div>
  <div class="footer">www.kestrelprops.co.za</div>
</section>

<!-- 21 bar chart -->
<section class="slide">
  <div class="brand">Kestrel<br>Properties</div>
  <div class="slide-title" style="left:19px"><b>CHART</b> AND DIAGRAM SLIDE</div>
  <svg style="position:absolute;left:26px;top:40px" width="120" height="80" font-family="Roboto,sans-serif" font-size="2.3" fill="#999">
    <line x1="16" y1="5" x2="16" y2="64" stroke="#ddd" stroke-width=".4"/>
    <line x1="16" y1="64" x2="118" y2="64" stroke="#ccc" stroke-width=".4"/>
    <text x="10" y="7">40</text><text x="10" y="22">30</text><text x="10" y="36">20</text><text x="10" y="50">10</text><text x="12" y="65">0</text>
    <rect x="26" y="46" width="5" height="18" fill="#333"/><rect x="32" y="26" width="5" height="38" fill="var(--red)"/>
    <rect x="48" y="30" width="5" height="34" fill="#333"/><rect x="54" y="6" width="5" height="58" fill="var(--red)"/>
    <rect x="70" y="40" width="5" height="24" fill="#333"/><rect x="76" y="22" width="5" height="42" fill="var(--red)"/>
    <rect x="92" y="36" width="5" height="28" fill="#333"/><rect x="98" y="14" width="5" height="50" fill="var(--red)"/>
    <text x="28" y="70">2021</text><text x="50" y="70">2022</text><text x="72" y="70">2023</text><text x="94" y="70">2024</text>
    <rect x="40" y="74" width="3" height="2" fill="var(--red)"/><text x="44" y="76">Sales</text>
    <rect x="62" y="74" width="3" height="2" fill="#333"/><text x="66" y="76">Costs</text>
  </svg>
  <div style="position:absolute;left:160px;top:42px;width:72px">
    <div class="heading">• Heading text</div><div class="body-text" style="margin-bottom:6px">Short text about the numbers shown here.</div>
    <div class="heading">• Heading text</div><div class="body-text" style="margin-bottom:6px">Short text about the numbers shown here.</div>
    <div class="heading">• Heading text</div><div class="body-text">Short text about the numbers shown here.</div>
  </div>
  <div class="footer">www.kestrelprops.co.za</div>
</section>

<!-- 22 process -->
<section class="slide">
  <div class="brand">Kestrel<br>Properties</div>
  <div class="slide-title" style="left:19px"><b>PROCCESS</b> SLIDE</div>
  <svg style="position:absolute;left:20px;top:50px" width="215" height="20">
    <polygon points="0,2 36,2 42,10 36,18 0,18 6,10" fill="#333"/>
    <polygon points="41,2 77,2 83,10 77,18 41,18 47,10" fill="var(--red)"/>
    <polygon points="82,2 118,2 124,10 118,18 82,18 88,10" fill="#333"/>
    <polygon points="123,2 159,2 165,10 159,18 123,18 129,10" fill="var(--red)"/>
    <polygon points="164,2 200,2 206,10 200,18 164,18 170,10" fill="#333"/>
    <use href="#i-search" x="18" y="6" width="8" height="8"/>
    <use href="#i-badge" x="59" y="6" width="8" height="8"/>
    <use href="#i-doc" x="100" y="6" width="8" height="8"/>
    <use href="#i-chart" x="141" y="6" width="8" height="8"/>
    <use href="#i-home" x="182" y="6" width="8" height="8"/>
  </svg>
  <div style="position:absolute;left:24px;top:74px;display:flex;gap:5px">
    <div style="width:36px"><div class="heading">Step 1</div><div class="body-text">Short text about the first step.</div></div>
    <div style="width:36px"><div class="heading">Step 2</div><div class="body-text">Short text about the next step.</div></div>
    <div style="width:36px"><div class="heading">Step 3</div><div class="body-text">Short text about the next step.</div></div>
    <div style="width:36px"><div class="heading">Step 4</div><div class="body-text">Short text about the next step.</div></div>
    <div style="width:36px"><div class="heading">Step 5</div><div class="body-text">Short text about the last step.</div></div>
  </div>
  <div class="footer">www.kestrelprops.co.za</div>
</section>

<!-- 23 section break -->
<section class="slide">
  <div class="photo" style="inset:0;background:linear-gradient(160deg,#d5d5d5 0%,#8f8f8f 55%,#3a3a3a 100%)" role="img" aria-label="Black and white photo of a coffee cup on a table"></div>
  <div style="position:absolute;left:0;top:86px;width:90px;height:54px;background:rgba(140,43,31,.9);color:#fff;padding:9px 0 0 30px">
    <div style="font-size:14px;font-weight:700;line-height:1">01.</div>
    <div style="font-size:5px;margin-top:3px">SECTION BREAK</div>
  </div>
</section>

<!-- 24 thank you -->
<section class="slide">
  <div style="position:absolute;left:0;top:0;width:250px;height:90px;background:var(--red)" role="img" aria-label="Red-tinted photo of houses"></div>
  <div style="position:absolute;left:0;width:250px;top:40px;text-align:center;color:#fff;font-size:6.6px">THANK YOU FOR WATCHING</div>
  <div style="position:absolute;left:0;width:250px;top:50px;text-align:center;color:#f0d6d2;font-size:2.4px">For more information please contact us</div>
  <div class="brand-box" style="left:46px;top:96px;width:48px;height:24px;font-size:4.6px">Kestrel<br>Properties</div>
  <div style="position:absolute;left:126px;top:94px;width:.5px;height:34px;background:var(--line)"></div>
  <div class="body-text" style="position:absolute;left:148px;top:95px;font-size:2.3px;line-height:2">
    <div>⌖ 22 Acacia Lane, Marlow Ridge 4410</div>
    <div>✆ +00 10 555 0142</div>
    <div>✆ +00 10 555 0143</div>
    <div>✉ hello@kestrelprops.co.za</div>
  </div>
  <div class="footer" style="height:3px"></div>
</section>

</main>
</body>
</html>
```